Wine Label Logo NEW name too

We would like to see this done in more colors but, lighter ones too. the dark colors don't show up that well. Can you also do some on white wine and not just red wine?

Also, we aren't sure we will use the name Plumvelle and wonder if you could use the name Nutmeadow with the same design to see how that looks, as well?

new wine label for a brand called Plumvelle (one word) and is targeted to go after 21-40 year olds. Probably more women than men. There will be Plumvelle Red, Plumvelle White, Plumvelle Cabernet, etc. the profile of the wine will be sweet...duh!!

would love you to come up with some TAG LINE ideas, as well. Size should be between 2 1/2 to 3 inches wide and 5 to 6 inches long. Needs place holders for varietal, Cabernet. 13.5% alcohol, area wil be California. I suggest you look at a bunch of wine labels to better understand this brief.

The final design should communicate fun, sweet, wine, young, hip

Wine labels matter. Period. Now, attempting to define “fun and contemporary” is nigh on impossible, but I think it would be safe to assume that this could mean “non-traditional.” Let’s face it. Design matters to millennial consumers. Quill, Tern Lodges, Hearthline Magazine – these brands are not ONLY for millennials by any means (well, maybe Tern), but design is top priority for these brands, and these brands have top priority for millennials. Feel free to do the math. If we spend money on something, we expect it to be beautiful and often times we expect social purchases like wine to act as a public reflection of our tastes and personality. This latter expectation is no different than any other generation (if arguably more intense due to our intrinsic personal branding tendencies); however, our personalities and what we are reflecting out to our peers IS different.
Updates

What about a label that is 2 1/2 to 3 inches wide and 5-6 inches long and looks like a white or off white piece of paper that has had berries poured across it with some stains and the name Plumvelle Cabernet as the logo on the label?  Needs space for the AVA area grown to say California and the vintage 2011 and alcohol level in small letters 12.3%. 

Look at some wine labels to get a unique idea. Needs to appeal to 21-40 year old women. Needs to denote the wine is sweet

Reason: two partners are out of the country and I want them involved in the choice

Target Market(s)

Industry/Entity Type

Social

Logo Text

Plumvelle Cabernet

Logo styles of interest
Pictorial/Combination Logo
Abstract Logo
Wordmark Logo

```html
<!DOCTYPE html>
<html lang="en">
<head>
<meta charset="utf-8">
<title>Plumvelle Wine Label</title>
<link rel="stylesheet" href="https://fonts.googleapis.com/css2?family=Nothing+You+Could+Do&family=Open+Sans:wght@400;700&display=swap">
<style>
  :root {
    --page: #ffffff;
    --ink: #231f20;
    --red: #ed1c24;
    --blue: #29abe2;
    --pink: #e6197a;
    --cream-top: #f8dfae;
    --cream-bottom: #fcf0d4;
    --cream-band: #fcf3dc;
    --script: "Nothing You Could Do", cursive;
    --sans: "Open Sans", Arial, sans-serif;
  }
  * { margin: 0; padding: 0; box-sizing: border-box; }
  html, body { width: 1200px; height: 900px; overflow: hidden; background: var(--page); }
  .canvas { position: relative; width: 1200px; height: 900px; }

  .label {
    position: absolute; left: 158px; top: 143px; width: 461px; height: 613px;
    background: var(--page); border-radius: 10px; overflow: hidden;
  }
  .label__cap { position: absolute; left: 0; right: 0; height: 12px; background: var(--red); }
  .label__cap--top { top: 0; }
  .label__cap--bottom { bottom: 0; }
  .label__hero {
    position: absolute; left: 0; right: 0; top: 12px; height: 366px;
    background: linear-gradient(var(--cream-top), var(--cream-bottom));
    border-left: 1px solid #f4a6a0; border-right: 1px solid #f4a6a0;
    border-radius: 8px 8px 0 0;
  }
  .label__foot {
    position: absolute; left: 0; right: 0; bottom: 12px; height: 50px;
    background: var(--cream-band);
    border-left: 1px solid #f4a6a0; border-right: 1px solid #f4a6a0;
    border-radius: 0 0 8px 8px;
  }
  .label__region {
    position: absolute; left: 0; right: 0; top: 418px; text-align: center;
    font-family: var(--script); font-size: 27px; color: var(--ink);
  }
  .label__varietal {
    position: absolute; left: 0; right: 0; top: 460px; text-align: center;
    font-family: var(--sans); font-weight: 700; font-size: 29px; color: var(--red);
  }
  .label__vintage {
    position: absolute; left: 0; right: 0; top: 506px; text-align: center;
    font-family: var(--sans); font-weight: 700; font-size: 19px; color: var(--ink);
  }
  .label__volume {
    position: absolute; right: 14px; top: 567px;
    font-family: var(--sans); font-size: 13px; color: var(--ink);
  }

  .brand { position: absolute; color: var(--ink); font-family: var(--script); line-height: 1; }
  .brand__name { position: absolute; left: 0; top: 0; white-space: nowrap; }
  .brand__variant { position: absolute; white-space: nowrap; }
  .brand__dot {
    position: absolute; border-radius: 50%; border: 5px solid currentColor;
    background: var(--cream-bottom);
  }
  .brand--red .brand__dot { color: var(--red); }
  .brand--white .brand__dot { color: var(--blue); }
  .brand--pink .brand__dot { color: var(--pink); }

  .brand.brand--label { left: 60px; top: 190px; width: 350px; height: 120px; font-size: 50px; }
  .brand--label .brand__variant { left: 185px; top: 56px; font-size: 44px; }
  .brand--label .brand__dot { left: 245px; top: -55px; width: 100px; height: 100px; }

  .brand--aside { left: 700px; width: 360px; height: 110px; font-size: 44px; }
  .brand--aside .brand__variant { font-size: 40px; top: 52px; }
  .brand--aside .brand__dot { left: 245px; top: -40px; width: 96px; height: 96px; }
  .brand--aside.brand--red { top: 190px; }
  .brand--aside.brand--red .brand__variant { left: 185px; }
  .brand--aside.brand--white { top: 437px; }
  .brand--aside.brand--white .brand__variant { left: 165px; }
  .brand--aside.brand--pink { top: 650px; }
  .brand--aside.brand--pink .brand__variant { left: 180px; }
</style>
</head>
<body>
<main class="canvas">
  <section class="label">
    <div class="label__cap label__cap--top"></div>
    <div class="label__hero"></div>
    <div class="brand brand--label brand--red">
      <span class="brand__dot"></span>
      <span class="brand__name">Plumvelle</span>
      <span class="brand__variant">Red</span>
    </div>
    <p class="label__region">Paso Robles</p>
    <p class="label__varietal">Cabernet Sauvignon</p>
    <p class="label__vintage">2012</p>
    <div class="label__foot"></div>
    <p class="label__volume">12.3% vol 75cl</p>
    <div class="label__cap label__cap--bottom"></div>
  </section>

  <div class="brand brand--aside brand--red">
    <span class="brand__dot"></span>
    <span class="brand__name">Plumvelle</span>
    <span class="brand__variant">Red</span>
  </div>
  <div class="brand brand--aside brand--white">
    <span class="brand__dot"></span>
    <span class="brand__name">Plumvelle</span>
    <span class="brand__variant">White</span>
  </div>
  <div class="brand brand--aside brand--pink">
    <span class="brand__dot"></span>
    <span class="brand__name">Plumvelle</span>
    <span class="brand__variant">Pink</span>
  </div>
</main>
</body>
</html>
```